Business Card Upgrade

I have designed our business card using our new logo. I think it needs imporovements. We used to have two cards for our business. One card was for our software business, and the other was for our consulting business. We are now in the process of combining our websites, marketing, name, and a new logo.

Our goal is to have a really sharp professional logo. One reason I designed the card the way I did was that our Titles are sometimes long, and by separating the person's name and title, it shows up very well and the title can be adjusted no matter how long it is. Sometimes the title can be 4 or 5 words or more.

We really like our logo on black as it shows up very nice. Our PMS colors are as follows: 368C and 459C.

The Designer that will be working with us will need to deliver the following:

The front and back of the Business Card Design will need to be delivered in a high quality JPEG, and
The front and back of the Business Card Design in Illustrator Format .ai
Any fonts will need to be sent to us if they are not standard and are required to open the Illustrator file correctly.

To help us get a good idea of the card with a title, please use the title: " Director of Software Development "

NOTE: The chosen designer will be selected to design our new letterhead within 2 weeks from the closing of this contest.

To help us make sure the card design works with longer titles, please use the followign job title on the card:  

"Director of Software and Product Development"

 

ALL DESIGNERS:

1. I appreciate the different angles you are showing the cards, but please be sure and always show the direct view, so I can see the layout and what the person I hand the card will see.

2. Please do not use white.  Please use off white as I don't care for white cards and they get dirty easy and do not represent the designs well.

Dear Designers,

Please provide samples straight one as a viewer of the card will see.  Some of the angles that are presented make it impossible to tell how everything fits, and sometimes even makes areas look skewed. So, please provide a straight sample view.

Pinnacle 400 company executives such as Vice Presidents, and Directors

Software

• Professional looking Card.

Our customers are Directors, Vice Presidents, and Presidents of companies as large as Pinnacle 400 companies. The card needs to get attention wile still looking professional.

Delivery of the finished product in Illustrator Format with any fonts needed to edit the text or open the file.

The card will be a heavy stock with a soft touch coating for that silk feel.

```html
<!DOCTYPE html>
<html lang="en">
<head>
<meta charset="utf-8">
<title>Harbor Trade Corporation – Business Card</title>
<link rel="stylesheet" href="https://fonts.googleapis.com/css2?family=Open+Sans:wght@400;600;700&family=Montserrat:wght@500;600&display=swap">
<style>
  :root {
    --backdrop: #8a4f26;
    --card: #121212;
    --card-edge: #1e1e1e;
    --green: #5db043;
    --cream: #e4daa2;
    --text-light: #e9e4c4;
  }
  * { margin: 0; padding: 0; box-sizing: border-box; }
  html, body { width: 1200px; height: 1000px; overflow: hidden; }
  body {
    background: var(--backdrop);
    font-family: "Open Sans", Arial, sans-serif;
    position: relative;
  }
  .card {
    position: absolute;
    width: 386px;
    height: 684px;
    border-radius: 28px;
    background: radial-gradient(ellipse at 50% 40%, #1c1c1c 0%, var(--card) 70%);
    border: 2px solid var(--card-edge);
    box-shadow: 0 6px 16px rgba(0,0,0,.45);
  }
  .card--front { left: 198px; top: 92px; }
  .card--back  { left: 668px; top: 262px; }

  .brand-name {
    position: absolute;
    left: 0; right: 0;
    text-align: center;
    font-family: "Montserrat", sans-serif;
    font-weight: 600;
    color: var(--green);
    line-height: 1.1;
  }
  .card--front .brand-name { top: 88px; font-size: 27px; letter-spacing: 1px; }
  .card--back .brand-name  { top: 205px; font-size: 44px; letter-spacing: 1px; }
  .brand-name span { display: block; }
  .card--front .brand-name .brand-sub { font-size: 16px; letter-spacing: 5px; }
  .card--back .brand-name .brand-sub { font-size: 26px; letter-spacing: 8px; }

  .accent-bar { position: absolute; left: -2px; width: 8px; }
  .accent-bar--name { top: 294px; height: 46px; background: var(--cream); }
  .accent-bar--contact { top: 380px; height: 132px; background: var(--green); }

  .person { position: absolute; left: 42px; top: 292px; }
  .person-name {
    font-family: "Montserrat", sans-serif;
    font-weight: 500;
    font-size: 24px;
    color: var(--green);
    letter-spacing: .5px;
  }
  .person-title { font-size: 16px; color: var(--text-light); margin-top: 2px; margin-left: 3px; }

  .contact-list { position: absolute; left: 44px; top: 391px; list-style: none; }
  .contact-list li {
    display: flex; align-items: flex-start;
    font-size: 15px; color: var(--text-light); line-height: 20px; margin-bottom: 4px;
  }
  .contact-list svg { width: 14px; height: 14px; margin: 3px 8px 0 0; flex: none; fill: var(--green); }

  .services {
    position: absolute; left: 0; right: 0; text-align: center;
    font-size: 15px; line-height: 23px; letter-spacing: .3px;
  }
  .services .divider { margin: 0 4px; }
  .card--front .services { top: 577px; color: var(--cream); }
  .card--front .services .divider { color: var(--green); }
  .card--back .services { top: 405px; color: var(--green); }
  .card--back .services .divider { color: var(--cream); }

  .tagline {
    position: absolute; left: 0; right: 0; text-align: center;
    font-size: 8px; font-weight: 600; letter-spacing: .2px;
  }
  .card--front .tagline { top: 643px; color: var(--green); }
  .card--front .tagline b { color: var(--cream); }
  .card--back .tagline { top: 460px; color: var(--cream); }
  .card--back .tagline b { color: var(--green); }

  .web-address {
    position: absolute; left: 0; right: 0; top: 644px; text-align: center;
    font-size: 17px; font-weight: 700; color: var(--cream); letter-spacing: .3px;
  }
</style>
</head>
<body>

<section class="card card--front" aria-label="Card front">
  <div class="brand-name"><span>HARBOR TRADE</span><span class="brand-sub">CORPORATION</span></div>

  <div class="accent-bar accent-bar--name"></div>
  <div class="person">
    <p class="person-name">DANA WHITFIELD</p>
    <p class="person-title">Director of Software Development</p>
  </div>

  <div class="accent-bar accent-bar--contact"></div>
  <ul class="contact-list">
    <li><svg viewBox="0 0 16 16" aria-hidden="true"><path d="M3 2h3l1 3-2 1a9 9 0 0 0 5 5l1-2 3 1v3c0 1-1 1-1 1C7 14 2 9 2 3c0 0 0-1 1-1z"/></svg>+ 555.010.2437</li>
    <li><svg viewBox="0 0 16 16" aria-hidden="true"><path d="M1 3h14v10H1z M2 4l6 5 6-5" fill="none" stroke="#5db043" stroke-width="1.6"/></svg>dwhitfield@harbortradeco.com</li>
    <li><svg viewBox="0 0 16 16" aria-hidden="true"><g fill="none" stroke="#5db043" stroke-width="1.3"><circle cx="8" cy="8" r="6.5"/><ellipse cx="8" cy="8" rx="3" ry="6.5"/><path d="M1.5 8h13"/></g></svg>harbortradeco.com</li>
    <li><svg viewBox="0 0 16 16" aria-hidden="true"><path d="M8 1a5 5 0 0 0-5 5c0 4 5 9 5 9s5-5 5-9a5 5 0 0 0-5-5zm0 7a2 2 0 1 1 0-4 2 2 0 0 1 0 4z"/></svg><span>418 Quarry Lane<br>Eastport, AL 36100</span></li>
  </ul>

  <p class="services">CONSULTING<span class="divider">|</span>SOFTWARE<br>OPERATIONS<span class="divider">|</span>ADMINISTRATION</p>
  <p class="tagline">THE ONLY FRIM WITH ENOUGH EXPERTISE TO OFFER EVERY <b>FTZ</b> SOLUTIONS</p>
</section>

<section class="card card--back" aria-label="Card back">
  <div class="brand-name"><span>HARBOR TRADE</span><span class="brand-sub">CORPORATION</span></div>
  <p class="services">CONSULTING<span class="divider">|</span>SOFTWARE<br>OPERATIONS<span class="divider">|</span>ADMINISTRATION</p>
  <p class="tagline">THE ONLY FRIM WITH ENOUGH EXPERTISE TO OFFER EVERY <b>FTZ</b> SOLUTIONS</p>
  <p class="web-address">WWW.HARBORTRADECO.COM</p>
</section>

</body>
</html>
```